Marlow Crossing Alliance Needs Posters for Next Wave Mobility Expo

Background Information
Background on organization:
The Marlow Crossing Alliance (MCA) is a next-generation community platform that connects, advocates for, and advances the goals of the world’s leading innovation ecosystem. We are a membership-based organization in Cambridge, MA that represents nearly 200 top companies, including: Zintrex, Pallowby, BQU, Vorn, Celvara, Holtam, and many other life sciences, technology, biotech, retail, non-profit, research and academic institutions. Learn more about the MCA on our website: www.marlowcx.org
Background on initiative:
The Boston area is dealing with significant traffic congestion. We know that the pain of getting in and out of Marlow Crossing is a consistent issue. The Marlow Crossing Alliance acknowledges this pain point and is working to collaborate on hyper-local solutions through the MCA Mobility UPLIFT - a year-long project with a series of experiments and pilots that will lead to a summit revealing results and sharing inspiring case studies.
Background on event:
Event title: Next Wave Mobility Expo
Target audience: 500-1,000 employees & residents of Marlow Crossing - primarily adults who work in biotech, tech, pharma industries who are early tech adopters.
Event description:
We're kicking off the MCA Mobility UPLIFT with an employee-centric, experiential event where employees and residents in Marlow can come out and ride 'futuristic' personal transportation modes. Don’t just watch cool videos on Vidloom! Join us at the Next Wave Mobility Expo and actually ride a Quell/Wren e-bike, try the Ravelpod hoverboard, learn about autonomous cars and planes.
Date: Tuesday, October 23rd (Rain Date: Thursday, October 25th)
Time: 11 AM - 12 PM
Location: Elmstead Court, near 318 Marlow St
Sponsors: Marlow Crossing Alliance, GenoVia
Featuring: Wren, Quell, Trundix, City Works Office, and other sponsors
Creative Brief
Content must include:
Title of event
Date
Location
Time
“Presented by the Marlow Crossing Alliance”
Logos of sponsors and vendors: Quell, Wren, Trundix, GenoVia, MCA and leave space for 4 other companies.
Copy: “You’re invited to come out and ride 'futuristic' personal transportation modes, such as e-scooters and hoverboards. Learn also about autonomous cars and planes.”
Look and feel:
Futuristic
Professional font (no Comic Sans)
Easy to read
Eye-catching
Can include pictures (either of people riding different modes of transpo or futuristic mock up)
Dimensions:
One-sided Posters, 8.5”x11” and 24” x 36”
Digital ‘postcards’ (4”x6”) for newsletters and digital invitation (can be the same design as poster)
Double sided-postcards (half of A4) to print handout in person (double sided in content)
Sidewalk arrows (18” x 12.5”) - see attached for context
PowerPoint slide (10" x 7.5") for digital elevator signage
Colors
Designer to choose colors to be used in the design.
Look and feel
Each slider illustrates characteristics of the customer's brand and the style your logo design should communicate.

```html
<!DOCTYPE html>
<html lang="en">
<head>
<meta charset="utf-8">
<title>Next Wave Mobility Expo Poster</title>
<link href="https://fonts.googleapis.com/css2?family=Montserrat:wght@400;500;600;700&family=Arimo:wght@400;700&display=swap" rel="stylesheet">
<style>
  :root {
    --teal: #1a8f8c;
    --teal-dark: #137876;
    --teal-light: #2aa6a2;
    --title-soft: #d9dcdc;
    --ink: #222;
    --ink-soft: #333;
    --strip: #f3f4f4;
    --backdrop: #2b2d2f;
  }
  * { margin: 0; padding: 0; box-sizing: border-box; }
  html, body { width: 1200px; height: 1200px; overflow: hidden; }
  body { background: var(--backdrop); position: relative; font-family: "Montserrat", sans-serif; }
  .poster {
    position: absolute; left: 155px; top: 25px; width: 889px; height: 1150px;
    background: #fff; overflow: hidden;
  }
  .hero-photo {
    position: absolute; left: 0; top: 0; width: 889px; height: 573px;
    background: linear-gradient(180deg, #eef2f3 0%, #dfe6e8 45%, #8a8580 80%, #5e5a56 100%);
  }
  .brand {
    position: absolute; top: 38px; left: 0; width: 100%;
    display: flex; justify-content: center; align-items: center; gap: 12px;
  }
  .brand-mark { width: 88px; height: 88px; background: var(--teal); }
  .brand-text { color: var(--teal); }
  .brand-name { font-weight: 700; font-size: 28px; line-height: 1.1; }
  .brand-tagline { font-weight: 400; font-size: 19px; margin-top: 4px; }
  .title-banner {
    position: absolute; left: 98px; top: 496px; width: 711px; height: 130px;
    background: linear-gradient(180deg, var(--teal-light), var(--teal-dark));
    border-radius: 5px; box-shadow: 0 10px 14px -8px rgba(0,0,0,.45);
    text-align: center; color: #fff; letter-spacing: 2px;
  }
  .title-line1 { font-weight: 600; font-size: 38px; color: var(--title-soft); margin-top: 18px; line-height: 1.2; }
  .title-line2 { font-weight: 700; font-size: 38px; line-height: 1.25; }
  .title-line2 .soft { font-weight: 600; color: var(--title-soft); }
  .presented { position: absolute; top: 643px; width: 100%; text-align: center; font-size: 19px; color: var(--ink-soft); }
  .presenter { position: absolute; top: 669px; width: 100%; text-align: center; font-size: 20px; font-weight: 600; color: var(--teal); letter-spacing: 1px; }
  .invite { position: absolute; top: 698px; left: 0; width: 100%; text-align: center; font-size: 15px; line-height: 19px; color: var(--ink-soft); letter-spacing: .3px; white-space: nowrap; }
  .details {
    position: absolute; left: 176px; top: 761px; width: 537px; height: 214px;
    border: 1.5px solid var(--teal); text-align: center;
    font-family: "Arimo", sans-serif; color: var(--ink); font-size: 25px;
  }
  .details .label { color: var(--teal); font-weight: 700; }
  .details strong { font-weight: 700; }
  .row-date { margin-top: 12px; }
  .row-rain { margin-top: 2px; }
  .row-time { margin-top: 14px; }
  .row-loc-label { margin-top: 12px; }
  .sponsors-label { position: absolute; top: 1002px; width: 100%; text-align: center; font-size: 19px; color: var(--ink-soft); letter-spacing: .5px; }
  .sponsor-strip {
    position: absolute; left: 42px; top: 1030px; width: 805px; height: 92px;
    background: var(--strip); display: flex; align-items: center; justify-content: space-around;
  }
  .sponsor { display: flex; align-items: center; gap: 6px; font-weight: 600; font-size: 17px; }
  .sponsor-dot { width: 26px; height: 26px; border-radius: 50%; }
  .sponsor-sq { width: 26px; height: 26px; }
  .s-quell { color: #7dc22a; } .s-quell .sponsor-dot { background: #7dc22a; }
  .s-genovia { color: #1f6fb5; } .s-genovia .sponsor-sq { background: #1f6fb5; }
  .s-marlow { color: var(--teal); } .s-marlow .sponsor-sq { background: var(--teal); }
  .s-trundix { color: #222; } .s-trundix .sponsor-dot { background: #222; }
  .s-wren { color: #000; } .s-wren .sponsor-sq { background: #000; }
  .footer-band { position: absolute; left: 0; bottom: 0; width: 100%; height: 19px; background: var(--teal); }
</style>
</head>
<body>
  <main class="poster">
    <div class="hero-photo" role="img" aria-label="Photo of business professionals meeting around a conference table in a bright office"></div>

    <div class="brand">
      <div class="brand-mark"></div>
      <div class="brand-text">
        <div class="brand-name">Marlow Crossing</div>
        <div class="brand-tagline">Where Ideas Get Moving</div>
      </div>
    </div>

    <div class="title-banner">
      <div class="title-line1">NEXT WAVE</div>
      <div class="title-line2">MOBILITY <span class="soft">EXPO</span></div>
    </div>

    <p class="presented">Presented by</p>
    <p class="presenter">THE MARLOW CROSSING ALLIANCE</p>
    <p class="invite">You’re invited to come out and ride ’futuristic’ personal transportation modes, such<br>as e-scooters and hoverboards. Learn also about autonomous cars and planes.</p>

    <section class="details">
      <div class="row-date"><span class="label">DATE:</span> <strong>Tuesday, October 23rd</strong></div>
      <div class="row-rain">(Rain Date: Thursday, October 25th)</div>
      <div class="row-time"><span class="label">TIME:</span> <strong>11 AM - 12 PM</strong></div>
      <div class="row-loc-label"><span class="label">LOCATION:</span></div>
      <div>Elmstead Court, near 318 Marlow St</div>
    </section>

    <p class="sponsors-label">sponsors and vendors</p>
    <div class="sponsor-strip">
      <div class="sponsor s-quell"><span class="sponsor-dot"></span>QuellBike</div>
      <div class="sponsor s-genovia"><span class="sponsor-sq"></span>GenoVia Realty</div>
      <div class="sponsor s-marlow"><span class="sponsor-sq"></span>Marlow Crossing</div>
      <div class="sponsor s-trundix"><span class="sponsor-dot"></span>TRUNDIX</div>
      <div class="sponsor s-wren"><span class="sponsor-sq"></span>Wren</div>
    </div>

    <div class="footer-band"></div>
  </main>
</body>
</html>
```